Web Design Project for Web Agency

WHAT I NEED:
The design I need (PSD file) is for a microsite designed for employee recruitment for Brantley, a Web agency.
***Design for the 1st Page ONLY : "Manifeste"
OBJECTIVES OF THE WEBSITE:
1. To promote the agency's corporate culture and HR management principles.
2. To get people to apply on available jobs
ELEMENTS OF THE PAGE "MANIFESTE" :
1. Brantley logo (see attached files). Beside the logo must be the word "Carrières" ("Careers" in english)
***The logo is not final and there is NO branding for Brantley yet. That is why there are multiple files. So please feel free to be creative!
2. Main menu : 4 sections
Manifeste | Opportunités | Brantly | Postuler
3. Manifeste :
This page is the home page. It will present 2 main sections :
a. The agency's corporate culture :
- Title of the page is a question : "Do you embrace Brantley's corporate culture?"
- Then, presentation of the 5 corporate values, each with a title and short description
- At the end of the list of values, we want a button that says "Apply now"
b. The agency's HR management principles :
- Title of the page is a question : "Do you see yourself working at Brantley?"
- Then, presentation of the 5 Management principles, each with a title and short description
- At the end of the list of principles, we want a button that says "Apply now"
VISUAL INSPIRATION
To create each section of the "Manifeste" page, we want a design that will fit with the corporate culture:
- Brantley is BOLD
- Brantley is PROUD
- Brantley is PROFESSIONAL
- Brantley is ELEGANT
- Brantley is REFINED
We want something slick and modern. Here are some Website's that we like that can be of inspiration:
- http://www.studio-vetrak.com/en/services
- http://quorvinpanels.com/

```html
<!DOCTYPE html>
<html lang="fr">
<head>
<meta charset="utf-8">
<title>Brantley Carrières — Manifeste</title>
<link rel="stylesheet" href="https://fonts.googleapis.com/css2?family=Montserrat:wght@400;600;700&family=Open+Sans:wght@400;600;700&display=swap">
<style>
:root{
  --orange:#f36f21;
  --orange-light:#f7a13c;
  --orange-pale:#fbc56a;
  --grey-text:#8c8c8c;
  --grey-heading:#b3b3b3;
  --grey-line:#d6d6d6;
  --grey-band:#e6e6e6;
  --ink:#222;
  --white:#fff;
}
*{box-sizing:border-box;margin:0;padding:0}
html,body{width:1200px;height:2840px;overflow:hidden;background:var(--white)}
body{font-family:"Open Sans",Arial,sans-serif;color:var(--ink)}

/* Header */
.site-header{height:142px;position:relative}
.brand{position:absolute;left:186px;top:46px;display:flex;align-items:flex-start}
.brand-block{display:flex;flex-direction:column}
.brand-name{font-family:"Montserrat",Arial,sans-serif;font-weight:700;font-size:44px;line-height:48px;color:var(--orange);letter-spacing:-1px}
.brand-tagline{font-family:"Montserrat",Arial,sans-serif;font-size:10px;letter-spacing:4px;color:#555;text-transform:uppercase;margin-top:2px;padding-left:4px}
.brand-section{font-family:"Montserrat",Arial,sans-serif;font-weight:600;font-size:26px;color:var(--grey-heading);border-left:2px solid var(--grey-line);margin-left:18px;padding-left:14px;line-height:38px;margin-top:6px}
.main-nav{position:absolute;right:200px;top:88px;display:flex}
.main-nav a{font-family:"Open Sans",Arial,sans-serif;font-weight:700;font-size:11px;color:var(--orange);text-decoration:none;text-transform:uppercase;padding:0 10px;border-left:1px solid var(--grey-line);line-height:14px}
.main-nav a:first-child{border-left:0}
.site-footer .main-nav a:last-child{padding-right:0}

/* Hero */
.hero{height:310px;background:linear-gradient(115deg,#ee7a1c 0%,#f39a2d 40%,#f7b545 70%,#f39a30 100%);display:flex;align-items:center;justify-content:center}
.hero-title{font-family:"Montserrat",Arial,sans-serif;font-weight:700;font-size:37px;line-height:49px;letter-spacing:10px;color:var(--white);text-align:center;text-transform:uppercase}

/* Section label */
.section-label{display:flex;align-items:center;justify-content:center;margin:44px auto 0;width:820px}
.section-label::before,.section-label::after{content:"";flex:1;height:2px;background:var(--grey-line)}
.section-label span{font-family:"Montserrat",Arial,sans-serif;font-weight:700;font-size:12px;letter-spacing:3px;color:var(--orange);text-transform:uppercase;padding:0 42px}

/* Cards */
.card-grid{margin-top:58px}
.card-row{display:flex;justify-content:center;gap:8px}
.card-row + .card-row{margin-top:44px}
.card{width:280px;text-align:center}
.card-photo{width:164px;height:164px;border-radius:50%;border:5px solid var(--orange);margin:0 auto;background:radial-gradient(circle at 40% 40%,#e8e8e8 0%,#a9a9a9 55%,#4c4c4c 100%)}
.card-photo.dark{background:radial-gradient(circle at 50% 50%,#bdbdbd 0%,#6b6b6b 55%,#2c2c2c 100%)}
.card-photo.warm{background:radial-gradient(circle at 50% 50%,#c98d4a 0%,#8a8a8a 40%,#3a3a3a 100%)}
.card-title{font-family:"Open Sans",Arial,sans-serif;font-weight:700;font-size:11px;color:var(--grey-text);text-transform:uppercase;margin-top:28px;line-height:16px}
.card-text{width:240px;margin:16px auto 0;text-align:left;font-size:12.5px;line-height:25px;font-weight:600;color:var(--ink)}

/* Apply button */
.apply{display:flex;align-items:center;justify-content:center;width:812px;margin:56px auto 0}
.apply::before,.apply::after{content:"";flex:1;height:2px;background:var(--grey-line)}
.apply-button{display:block;width:160px;height:42px;margin:0 58px;background:var(--orange);color:var(--white);font-family:"Montserrat",Arial,sans-serif;font-weight:700;font-size:11px;letter-spacing:3px;text-transform:uppercase;text-align:center;line-height:42px;text-decoration:none}

/* Question heading */
.question{margin-top:104px;text-align:center;font-family:"Montserrat",Arial,sans-serif;font-weight:700;font-size:39px;line-height:51px;letter-spacing:11px;color:var(--grey-heading);text-transform:uppercase}
.question strong{color:var(--orange);font-weight:700}
.question + .section-label{margin-top:134px}

/* Footer */
.site-footer{margin-top:80px;height:134px;background:var(--grey-band);position:relative}
.site-footer .main-nav{left:258px;right:auto;top:58px}
.site-footer .main-nav a{padding:0 12px}
.site-footer .main-nav a:first-child{padding-left:0}
.site-footer .brand{left:654px;top:40px}
.site-footer .brand-name{color:#8e8e8e;font-size:38px;line-height:42px}
.site-footer .brand-tagline{color:#9a9a9a;font-size:9px}
.site-footer .brand-section{font-size:22px;line-height:32px;margin-top:4px}
.footer-meta{text-align:center;font-family:"Montserrat",Arial,sans-serif;font-size:10px;letter-spacing:3px;line-height:18px;color:#666;text-transform:uppercase;margin-top:14px}
.footer-meta .contact{color:var(--orange)}
.copyright{text-align:center;font-family:"Montserrat",Arial,sans-serif;font-size:10px;letter-spacing:3px;color:#666;text-transform:uppercase;margin-top:26px}
.copyright span{color:var(--orange)}
</style>
</head>
<body>

<header class="site-header">
  <div class="brand">
    <div class="brand-block">
      <span class="brand-name">Brantley</span>
      <span class="brand-tagline">Agence numérique</span>
    </div>
    <span class="brand-section">Carrières</span>
  </div>
  <nav class="main-nav">
    <a href="#">Manifeste</a><a href="#">Opportunités</a><a href="#">Brantly</a><a href="#">Postuler</a>
  </nav>
</header>

<section class="hero" role="img" aria-label="Warm orange background with a faint architectural grid">
  <h1 class="hero-title">Do you<br>embrace Brantley's<br>corporate culture?</h1>
</section>

<section class="values">
  <h2 class="section-label"><span>Brantley 5 corporate values</span></h2>
  <div class="card-grid">
    <div class="card-row">
      <article class="card"><div class="card-photo" role="img" aria-label="Black and white photo of a handshake"></div><h3 class="card-title">Brantley is bold</h3><p class="card-text">Lorem ipsum dolor sit amet, consectetur adipiscing elit. Sed pellentesque, purus sit amet pulvinar sollicitudin, nulla odio hen-</p></article>
      <article class="card"><div class="card-photo" role="img" aria-label="Black and white photo of colleagues joining hands"></div><h3 class="card-title">Brantley is proud</h3><p class="card-text">Lorem ipsum dolor sit amet, consectetur adipiscing elit. Sed pellentesque, purus sit amet pulvinar sollicitudin, nulla odio hen-</p></article>
      <article class="card"><div class="card-photo" role="img" aria-label="Black and white photo of team hands stacked together"></div><h3 class="card-title">Brantley is professional</h3><p class="card-text">Lorem ipsum dolor sit amet, consectetur adipiscing elit. Sed pellentesque, purus sit amet pulvinar sollicitudin, nulla odio hen-</p></article>
    </div>
    <div class="card-row">
      <article class="card"><div class="card-photo dark" role="img" aria-label="Black and white photo of clasped hands"></div><h3 class="card-title">Brantley is elegant</h3><p class="card-text">Lorem ipsum dolor sit amet, consectetur adipiscing elit. Sed pellentesque, purus sit amet pulvinar sollicitudin, nulla odio hen-</p></article>
      <article class="card"><div class="card-photo" role="img" aria-label="Black and white photo of a hand holding a business card"></div><h3 class="card-title">Brantley is refined</h3><p class="card-text">Lorem ipsum dolor sit amet, consectetur adipiscing elit. Sed pellentesque, purus sit amet pulvinar sollicitudin, nulla odio hen-</p></article>
    </div>
  </div>
  <div class="apply"><a class="apply-button" href="#">Apply now</a></div>
</section>

<h2 class="question">Do you see yourself<br>working at <strong>Brantley</strong>?</h2>

<section class="principles">
  <h2 class="section-label"><span>5 management principles</span></h2>
  <div class="card-grid">
    <div class="card-row">
      <article class="card"><div class="card-photo" role="img" aria-label="Black and white photo of a hand reaching upward"></div><h3 class="card-title">Set high objectives</h3><p class="card-text">Lorem ipsum dolor sit amet, consectetur adipiscing elit. Sed pellentesque, purus sit amet pulvinar sollicitudin, nulla odio hen-</p></article>
      <article class="card"><div class="card-photo dark" role="img" aria-label="Black and white photo of pencils in a cup"></div><h3 class="card-title">Set specific goals</h3><p class="card-text">Lorem ipsum dolor sit amet, consectetur adipiscing elit. Sed pellentesque, purus sit amet pulvinar sollicitudin, nulla odio hen-</p></article>
      <article class="card"><div class="card-photo" role="img" aria-label="Black and white photo of a hand with motion blur"></div><h3 class="card-title">Keep a passionate</h3><p class="card-text">Lorem ipsum dolor sit amet, consectetur adipiscing elit. Sed pellentesque, purus sit amet pulvinar sollicitudin, nulla odio hen-</p></article>
    </div>
    <div class="card-row">
      <article class="card"><div class="card-photo dark" role="img" aria-label="Black and white photo of interlocking gears"></div><h3 class="card-title">Solid team player</h3><p class="card-text">Lorem ipsum dolor sit amet, consectetur adipiscing elit. Sed pellentesque, purus sit amet pulvinar sollicitudin, nulla odio hen-</p></article>
      <article class="card"><div class="card-photo warm" role="img" aria-label="Close-up photo of a determined gaze with an amber accent"></div><h3 class="card-title">Face every challenge</h3><p class="card-text">Lorem ipsum dolor sit amet, consectetur adipiscing elit. Sed pellentesque, purus sit amet pulvinar sollicitudin, nulla odio hen-</p></article>
    </div>
  </div>
  <div class="apply"><a class="apply-button" href="#">Apply now</a></div>
</section>

<footer class="site-footer">
  <nav class="main-nav">
    <a href="#">Manifeste</a><a href="#">Opportunités</a><a href="#">Brantly</a><a href="#">Postuler</a>
  </nav>
  <div class="brand">
    <div class="brand-block">
      <span class="brand-name">Brantley</span>
      <span class="brand-tagline">Agence numérique</span>
    </div>
    <span class="brand-section">Carrières</span>
  </div>
</footer>
<div class="footer-meta">
  <p>Brantley, 42 Alder Row Suite 9, Lorem ipsum dolor sit amet, 5210, Mortem</p>
  <p class="contact">T: 1800-555012 . F: 700-555019 . E: enquiry@brantley.com</p>
</div>
<p class="copyright">Copyright ©2013 <span>Brantley Carrières</span></p>

</body>
</html>
```